Business card design needed

I need a business card design for a dog walking, dog minding and dog training business. Please refer to my website for the basic company colours and fonts I'm after. Planning on a double sided card, so all information doesn't need to be on the 'front' side.
Cheers

Industry/Entity Type

Dog Training

Contact Information for Business Card

Meadow Paws - happy hounds
Rua 0498307164
meadowpawsdemo.com.au
-walking
-holiday stays
-onsite care
-training and behavioural consultations

```html
<!DOCTYPE html>
<html lang="en">
<head>
<meta charset="utf-8">
<title>Meadow Paws – Business Card</title>
<link rel="stylesheet" href="https://fonts.googleapis.com/css2?family=Jost:wght@300;400&family=Arvo:wght@700&family=Space+Mono&display=swap">
<style>
  :root {
    --cream: #f0ebe4;
    --orange: #f15a24;
    --orange-soft: #f47c52;
    --grey: #7d7d7d;
    --ink: #111111;
    --white: #ffffff;
    --page: #ffffff;
  }
  * { margin: 0; padding: 0; box-sizing: border-box; }
  html, body { width: 1200px; height: 900px; overflow: hidden; background: var(--page); }
  body { position: relative; font-family: "Jost", sans-serif; }

  .card { position: absolute; left: 270px; width: 660px; overflow: hidden; }
  .card--front { top: 24px; height: 410px; background: var(--cream); }
  .card--back { top: 466px; height: 411px; background: var(--orange); }

  .brand { position: absolute; }
  .brand__name {
    display: block; font-family: "Jost", sans-serif; font-weight: 400;
    color: var(--orange); letter-spacing: 1px; line-height: 1; white-space: nowrap;
  }
  .brand__tagline {
    display: block; text-align: right; font-weight: 400; color: var(--ink);
    line-height: 1; margin-top: 4px;
  }
  .card--front .brand { left: 160px; top: 124px; }
  .card--front .brand__name { font-size: 54px; }
  .card--front .brand__tagline { font-size: 15px; }

  .photo-placeholder {
    position: absolute;
    background: radial-gradient(circle at 50% 40%, #d9b07a 0%, #c89a64 45%, rgba(240,235,228,0) 75%);
  }
  .card--front .photo-placeholder { left: 505px; top: 228px; width: 140px; height: 160px; }

  .website { position: absolute; left: 22px; top: 369px; font-size: 16px; color: var(--orange); }

  .back__top-band { position: absolute; left: 0; top: 0; width: 100%; height: 34px; background: var(--orange); }
  .back__header { position: absolute; left: 0; top: 34px; width: 100%; height: 120px; background: var(--cream); }
  .card--back .brand { left: 30px; top: 42px; }
  .card--back .brand__name { font-size: 36px; }
  .card--back .brand__tagline { font-size: 11px; }
  .card--back .photo-placeholder { left: 568px; top: 10px; width: 76px; height: 92px; }

  .contact { position: absolute; left: 30px; top: 160px; font-size: 44px; line-height: 1; white-space: nowrap; }
  .contact__name { color: var(--white); font-weight: 300; }
  .contact__phone { color: var(--ink); font-weight: 400; }

  .walkers-placeholder {
    position: absolute; left: 60px; top: 200px; width: 550px; height: 140px;
    background: linear-gradient(90deg, rgba(255,255,255,0.16), rgba(255,255,255,0.22), rgba(255,255,255,0.14));
    border-radius: 40px;
  }

  .services { position: absolute; left: 378px; top: 174px; color: var(--white); }
  .services__title { font-family: "Space Mono", monospace; font-size: 13px; letter-spacing: 1px; margin-bottom: 8px; }
  .services__list { list-style: none; padding-left: 26px; font-family: "Arvo", serif; font-weight: 700; font-size: 13.5px; line-height: 17.6px; }

  .credentials {
    position: absolute; left: 42px; top: 364px; color: var(--white);
    font-size: 13px; line-height: 17px; font-weight: 400;
  }
</style>
</head>
<body>
  <section class="card card--front">
    <div class="brand">
      <span class="brand__name">MEADOW PAWS</span>
      <span class="brand__tagline">happy hounds.</span>
    </div>
    <div class="photo-placeholder" role="img" aria-label="Photo of a sitting puppy looking up"></div>
    <p class="website">meadowpawsdemo.com.au</p>
  </section>

  <section class="card card--back">
    <div class="back__top-band"></div>
    <div class="back__header">
      <div class="brand">
        <span class="brand__name">MEADOW PAWS</span>
        <span class="brand__tagline">happy hounds.</span>
      </div>
      <div class="photo-placeholder" role="img" aria-label="Small photo of a sitting puppy"></div>
    </div>
    <div class="walkers-placeholder" role="img" aria-label="Faint silhouettes of a person walking dogs"></div>
    <p class="contact"><span class="contact__name">Rua</span> <span class="contact__phone">0498307164</span></p>
    <div class="services">
      <p class="services__title">SERVICES:</p>
      <ul class="services__list">
        <li>Group dog walk</li>
        <li>Group dog walk casual</li>
        <li>Solo dog walk</li>
        <li>Solo dog walk casual</li>
        <li>On site, in home care</li>
        <li>Hound holiday stay</li>
      </ul>
    </div>
    <p class="credentials">*Meadow Paws is run by a qualified dog behaviourist and trainer who is also an accredited pet first aider.<br>We hold pet care specific public liability insurance and carry a current police check.</p>
  </section>
</body>
</html>
```